NEW Website DESIGN for Brightwell Panes & Stoneworks Company

Brand New website, contemporary, clean, visual (images), not busy. ATTACHED IS OUR LOG THAT YOU MUST USE.

The company is called Brightwell Panes & Stoneworks (BrightwellPS)
www.brightwellps.com
The website should be www.brightwellpns.com
one page for glass one page for solid surfaces www.brightwellpanesplashes.co.uk
www.brightwellstoneworkss.co.uk

Target Market(s)

Hotels, Commercial projects, Small focus on residential

Industry/Entity Type

Construction

Number of Pages Required

5+ page

Font styles to use
Sans Serif

Requirements
Must have
• COLOURS AS PER OUR LOGO - WHITE/YELLOW/GREY - WHITE BACK GROUND
• CLEAR SIMPLE NAVIGATION - MODER CLEAN CUT - DESIGN FEEL
• LATEST NAVIGATION FOR IMAGES and text to include per project details
• WORK/PROJECT AREA - NEWS AREA - TEAM AREA/ABOUT US/CONTACT US
• NEW PAGEwww.brightwellpanesplashes.co.uk - NEW PAGE www.brightwellstoneworkss.co.uk
• PLEASE COPY THIS TYPE OF TEMPALTE
• https://www.harlowmead.co.uk/project/grand-halls/
• MOBILE READY
• WORDPRESS
• MODERN IMAGES INCLUDING VELMARA KESTRIN AND GLASS PROJECTS
Nice to have
• NEW DESIGN MODER FRESH
• WEBSITES I LIKE THE TEMPLATE SHOULD BE LIKE THE WEBSITE BELOW
• https://www.harlowmead.co.uk/
Should not have
• NOT Old fashion template, not busy NAVIGATION
• NO BLACK
• NO DARK GREYS
• NOT LOTS OF YELLOW
• RESDENTIAL IMAGES

```html
<!DOCTYPE html>
<html lang="en">
<head>
<meta charset="utf-8">
<title>Brightwell Panes &amp; Stoneworks – Solid Surfaces</title>
<link href="https://fonts.googleapis.com/css2?family=Montserrat:wght@500;600;700&family=Jost:wght@400;500&family=Roboto:wght@400;700&display=swap" rel="stylesheet">
<style>
:root{
  --yellow:#f2ea1f;
  --yellow-soft:#ece64a;
  --grey:#8a8a8a;
  --text:#1f1f1f;
  --text-soft:#555;
  --line:#e4e4e4;
  --white:#fff;
  --footer:#8c8c8c;
  --icon:#e8dc1a;
}
*{margin:0;padding:0;box-sizing:border-box}
html,body{width:780px;height:1200px;overflow:hidden;background:var(--white)}
body{position:relative;font-family:'Jost',sans-serif;color:var(--text)}

.hero{position:absolute;left:23px;top:92px;width:734px;height:314px;
  background:
    linear-gradient(180deg,rgba(255,255,255,0) 78%,rgba(60,58,55,.55) 100%),
    radial-gradient(ellipse 90px 24px at 680px 22px,#d9b85a 0%,rgba(217,184,90,0) 100%),
    linear-gradient(90deg,rgba(0,0,0,0) 0,rgba(0,0,0,0) 640px,rgba(230,236,238,.55) 660px,rgba(210,218,220,.6) 734px),
    radial-gradient(ellipse 60px 50px at 440px 180px,#f4efe2 0%,rgba(244,239,226,0) 100%),
    linear-gradient(90deg,#5e5a55 0%,#6f6a63 10%,#c9b98a 18%,#b5a98c 26%,#9c968e 34%,#cfc9be 46%,#e8e3d7 52%,#c9c3b6 58%,#e9dfbc 64%,#f0e6c4 70%,#cfc7b3 80%,#a9a59c 88%,#bfc3c2 100%);}

.brand-cap{position:absolute;left:-70px;top:-84px;width:300px;height:210px;border-radius:50%;background:var(--white)}
.brand{position:absolute;left:10px;top:12px;width:190px;text-align:center}
.brand-mark{width:64px;height:64px;border-radius:50%;border:6px solid var(--grey);margin:0 auto 13px}
.brand-name{font-family:'Montserrat',sans-serif;font-weight:600;font-size:9px;color:var(--grey);white-space:nowrap}

.nav{position:absolute;top:24px;left:284px;display:flex;height:43px;align-items:center}
.nav a{font-family:'Roboto',sans-serif;font-size:8px;font-weight:700;color:var(--text);text-decoration:none;
  padding:0 13px;height:43px;display:flex;align-items:center;border-right:1px solid var(--line)}
.nav a:last-child{border-right:none}
.nav a.active{background:var(--yellow);height:25px;margin:0 12px;padding:0 13px;border-right:none}
.nav a.before-active{border-right:none}

.intro{position:absolute;left:100px;top:455px;width:580px;text-align:center;font-size:8.4px;line-height:14px}
.intro p+p{margin-top:12px;color:var(--text-soft)}

.slider{position:absolute;left:0;top:618px;width:780px;height:278px}
.slide-side{position:absolute;top:0;height:278px;width:170px}
.slide-side.left{left:0;background:
  linear-gradient(170deg,rgba(255,255,255,0) 20%,rgba(255,255,255,.35) 32%,rgba(255,255,255,0) 40%),
  linear-gradient(180deg,#e9e23c 0%,#ebe44a 45%,#efe860 60%,#e6df3c 100%)}
.slide-side.right{right:0;background:
  linear-gradient(180deg,#f1eb5a 0%,#ece544 40%,#e2da3a 70%,#eee85c 100%)}
.slide-main{position:absolute;left:170px;top:0;width:440px;height:278px;
  background:
    linear-gradient(180deg,rgba(0,0,0,0) 0,rgba(0,0,0,0) 230px,rgba(240,236,228,.9) 250px,#ece8e0 278px),
    radial-gradient(ellipse 110px 40px at 220px 150px,#ffffff 0%,rgba(255,255,255,0) 100%),
    linear-gradient(90deg,#8e8a85 0%,#6d6a66 14%,#c7c2ba 22%,#dcd7cf 40%,#e3ded5 56%,#b99b62 66%,#a7a29b 76%,#9a968f 100%),
    linear-gradient(180deg,#8d8983 0%,#d6d2ca 40%,#a89b8a 70%,#ebe7df 100%);
  background-blend-mode:normal,normal,multiply,normal}
.slide-arrow{position:absolute;top:746px}

.contact-rule{position:absolute;left:334px;top:951px;width:76px;height:1px;background:var(--yellow)}
.contact-title{position:absolute;left:0;width:750px;top:964px;text-align:center;font-family:'Montserrat',sans-serif;
  font-weight:600;font-size:15px;color:var(--grey)}
.cards{position:absolute;top:1003px;left:92px;display:flex;gap:16px}
.card{width:188px;height:119px;border:1px solid var(--line);text-align:center;padding-top:24px}
.card svg{display:block;margin:0 auto 6px}
.card h3{font-family:'Montserrat',sans-serif;font-weight:700;font-size:9.5px;letter-spacing:.5px;margin-bottom:4px}
.card p{font-family:'Roboto',sans-serif;font-size:7.5px;line-height:10px}

.footer{position:absolute;left:0;top:1172px;width:780px;height:28px;background:var(--footer);color:var(--white);
  font-size:7px;display:flex;align-items:center;justify-content:space-between;padding:0 92px}
.social{display:flex;gap:8px}
.social span{width:7px;height:7px;border-radius:50%;background:var(--white)}
</style>
</head>
<body>
<div class="hero" role="img" aria-label="Hotel lobby interior with marble reception desk, gold patterned screens and lounge chairs"></div>
<div class="brand-cap"></div>
<div class="brand">
  <div class="brand-mark"></div>
  <div class="brand-name">Brightwell Panes &amp; Stoneworks</div>
</div>
<nav class="nav">
  <a href="#">Home</a><a href="#">About Us</a><a href="#" class="before-active">Glass</a><a href="#" class="active">Solid Surfaces</a><a href="#">Projects</a><a href="#">News</a><a href="#">Contact Us</a>
</nav>
<section class="intro">
  <p>Lorem ipsum dolor sit amet, consectetuer adipiscing elit, sed diam nonummy nibh euismod tincidunt ut laoreet dolore magna aliquam erat volutpat. Ut wisi enim ad minim veniam, quis nostrud exerci tation ullamcorper suscipit lobortis nisl ut aliquip ex ea commodo consequat. Duis autem vel eum iriure dolor in hendrerit in vulputate velit esse molestie consequat, vel illum dolore eu feugiat nulla facilisis at vero eros et accumsan et iusto odio dignissim qui blandit praesent luptatum zzril delenit augue duis dolore te feugait nulla facilisi.</p>
  <p>Lorem ipsum dolor sit amet, consectetuer adipiscing elit, sed diam nonummy nibh euismod tincidunt ut laoreet dolore magna aliquam erat volutpat. Ut wisi enim ad minim veniam, quis nostrud exerci tation ullamcorper suscipit lobortis nisl ut aliquip ex ea commodo consequat. Duis autem vel eum iriure dolor in hendrerit in vulputate velit esse molestie consequat, vel illum dolore eu feugiat nulla facilisis at vero eros et accumsan et iusto odio dignissim qui blandit praesent luptatum zzril delenit augue duis dolore te feugait nulla facilisi nonummy nibh euismod tincidunt ut laoreet dolore.</p>
</section>
<section class="slider">
  <div class="slide-side left" role="img" aria-label="Previous project: reception interior with yellow tint"></div>
  <div class="slide-main" role="img" aria-label="Hotel reception with white solid surface desk and lounge seating"></div>
  <div class="slide-side right" role="img" aria-label="Next project: bedroom interior with yellow tint"></div>
</section>
<svg class="slide-arrow" style="left:131px" width="22" height="22" viewBox="0 0 22 22"><circle cx="11" cy="11" r="10" fill="none" stroke="#555" stroke-width="1.6"/><path d="M16 11H6M10 7l-4 4 4 4" fill="none" stroke="#555" stroke-width="1.6"/></svg>
<svg class="slide-arrow" style="left:627px" width="22" height="22" viewBox="0 0 22 22"><circle cx="11" cy="11" r="10" fill="none" stroke="#555" stroke-width="1.6"/><path d="M6 11h10M12 7l4 4-4 4" fill="none" stroke="#555" stroke-width="1.6"/></svg>
<div class="contact-rule"></div>
<h2 class="contact-title">Contact Us</h2>
<section class="cards">
  <div class="card">
    <svg width="16" height="20" viewBox="0 0 16 20"><path d="M8 19s7-7 7-11.5A7 7 0 0 0 1 7.5C1 12 8 19 8 19z" fill="none" stroke="var(--icon)" stroke-width="1.2"/><circle cx="8" cy="7.5" r="2.5" fill="none" stroke="var(--icon)" stroke-width="1.2"/></svg>
    <h3>Address</h3>
    <p>Larkfield Holdings<br>Marlow Court Business Park<br>Fenwick Lane, Northam, NM4 2QT</p>
  </div>
  <div class="card">
    <svg width="22" height="22" viewBox="0 0 22 22"><path d="M5 3l3 0 1.5 4-2 1.5a10 10 0 0 0 5 5l1.5-2 4 1.5 0 3a2 2 0 0 1-2 2C9 18 4 13 3 5a2 2 0 0 1 2-2z" fill="none" stroke="var(--icon)" stroke-width="1.2"/><path d="M13 3a6 6 0 0 1 6 6M13 6a3 3 0 0 1 3 3" fill="none" stroke="var(--icon)" stroke-width="1.2"/></svg>
    <h3>Call Us</h3>
    <p>+ 44 (0)1632 960418</p>
  </div>
  <div class="card">
    <svg width="28" height="20" viewBox="0 0 28 20"><rect x="1" y="1" width="26" height="18" fill="none" stroke="var(--icon)" stroke-width="1.2"/><path d="M1 1l13 10L27 1M1 19l10-9M27 19l-10-9" fill="none" stroke="var(--icon)" stroke-width="1.2"/></svg>
    <h3>Mail Us</h3>
    <p>info@larkfield-hq.com</p>
  </div>
</section>
<footer class="footer">
  <span>Copyright © 2018 Brightwell Panes &amp; Stoneworks. All Rights Reserved.</span>
  <div class="social"><span></span><span></span><span></span><span></span></div>
</footer>
</body>
</html>
```